3 page designs for our Travel Company!!

Hi there!
We need 3 page designs to add to our travel website. We have include the PSD files of relevant web pages for you to use. We would like the new designs to fit in with the pages we already have designed please (colours, layout & style)
We require the following pages:
1. Hotel Search Page
2. Hotel Page
- For these pages, we are looking for an aesthetic design layout that fits in line with the layout of the pages we have designed. (PSD files 'Tour Page' & 'Tour Search Pages')
- We want to see imaginative ways of arranging the content in pleasant and 'easy to read' layouts.
3. Mobile View Page
- This is simply the design layout for the 'Mobile View'.
- We want you to illustrate how the drop down menus will work.
- Simplicity is key here. We want the menus to be easy to understand
- The 'Discover Cayman' menu is the only menu with multiple sub categories (You can see this in the PSD file named 'Drop Down Menu')
You can find our support documents here at https://www.filquarry.net/sh/7k21mdqzhrtt93p/QWxeLmPNvKrtaZu8fGh02bYRq?dl=0
Please feel free to get imaginative with unique ways these pages can be played out!
Thank you!

```html
<!DOCTYPE html>
<html lang="en">
<head>
<meta charset="utf-8">
<title>Caybound – Hotel Search</title>
<link href="https://fonts.googleapis.com/css2?family=Open+Sans:wght@300;400;600;700&display=swap" rel="stylesheet">
<style>
:root{
  --green:#9bcb3b;
  --blue:#1a6fd6;
  --ink:#333;
  --muted:#666;
  --page:#f1f1f1;
  --line:#d6d6d6;
  --white:#fff;
  --footer:#262626;
  --band-a:#1f63b5;
  --band-b:#3a86cf;
}
*{box-sizing:border-box;margin:0;padding:0}
html,body{width:731px;height:1200px;overflow:hidden}
body{font-family:"Open Sans",sans-serif;background:var(--page);color:var(--ink);position:relative}
.abs{position:absolute}
.btn{background:var(--green);color:#fff;font-weight:600;border-radius:3px;display:flex;align-items:center;justify-content:center}

/* header */
.site-header{left:0;top:0;width:731px;height:31px;background:var(--white);border-bottom:1px solid #e2e2e2}
.brand{left:105px;top:8px;display:flex;align-items:center;gap:4px;font-size:10px;font-weight:700;color:var(--blue)}
.brand i{width:9px;height:9px;background:var(--green);display:block}
.main-nav{left:202px;top:10px;display:flex;gap:11px;font-size:7px;color:#444}
.select{top:9px;height:13px;border:1px solid #ddd;border-radius:2px;font-size:6.5px;display:flex;align-items:center;padding:0 5px;gap:4px;color:#333}
.select svg{width:5px}
.login{left:580px;top:9px;width:46px;height:13px;font-size:6.5px}

/* search */
.search-field{top:36px;height:22px;background:var(--white);border:1px solid #e2e2e2;border-radius:2px;display:flex;align-items:center;gap:7px;padding-left:9px}
.search-field svg{width:10px;height:10px;fill:var(--blue)}
.search-field small{display:block;font-size:6px;color:#444;line-height:7px}
.search-field b{display:block;font-size:8px;font-weight:400;line-height:10px}
.search-btn{left:516px;top:36px;width:110px;height:22px;font-size:8px}
.rule{height:1px;background:var(--line)}

/* sidebar */
.map-card{left:105px;top:77px;width:169px;height:128px;background:var(--white);border-radius:3px;overflow:hidden}
.map-area{height:103px;background:linear-gradient(135deg,#a9d1f5 0%,#a9d1f5 40%,#e8e6df 55%,#dcdad2 100%)}
.map-card p{text-align:center;font-size:8px;color:#555;line-height:25px}
.filters{left:105px;top:214px;width:160px}
.filters h4{font-weight:400;font-size:7.5px;color:#333}
.filter-title{display:flex;align-items:center;gap:3px;margin-top:8px}
.price{display:flex;align-items:center;gap:3px;font-size:7.5px;margin-top:8px}
.price span{width:39px;height:13px;background:#fff;border:1px solid #ddd;border-radius:2px;font-size:5.5px;color:#888;display:flex;align-items:center;justify-content:center}
.group{border-top:1px solid var(--line);padding-top:6px;margin-top:7px}
.checks{list-style:none;margin-top:3px}
.checks li{height:14.6px;display:flex;align-items:center;gap:4px;font-size:7.5px;color:#555}
.box{width:7px;height:7px;border:1px solid #b9c4d3;border-radius:1px;background:#fff;display:flex;align-items:center;justify-content:center}
.box.on{background:var(--blue);border-color:var(--blue)}
.box.on::after{content:"";width:3px;height:1.5px;border-left:1px solid #fff;border-bottom:1px solid #fff;transform:rotate(-45deg) translate(0,-0.5px)}
.checks li.fade{opacity:.35}
.see-link{font-size:7.5px;color:var(--blue);margin-top:1px}
.divider-v{left:274px;top:224px;width:1px;height:560px;background:var(--line)}
.filter-btn{left:105px;top:761px;width:85px;height:23px;font-size:7.5px}

/* hotel cards */
.hotel{left:283px;width:343px;height:128px;background:var(--white);border-radius:3px;overflow:hidden}
.hotel .photo{position:absolute;left:0;top:0;width:128px;height:128px}
.arrow{position:absolute;top:56px;width:15px;height:15px;border-radius:50%;background:rgba(30,30,30,.75);display:flex;align-items:center;justify-content:center}
.arrow svg{width:6px;height:6px}
.dots{position:absolute;bottom:9px;left:0;width:128px;display:flex;justify-content:center;gap:3px}
.dots i{width:2px;height:2px;background:#fff;border-radius:50%}
.dots i:first-child{width:3.5px;height:3.5px}
.hotel h3{position:absolute;left:137px;top:9px;font-size:9.5px;font-weight:600;color:#333}
.reviews{position:absolute;right:9px;top:12px;font-size:6.5px;color:var(--blue)}
.loc{position:absolute;left:137px;top:25px;font-size:7.5px;display:flex;align-items:center;gap:2px}
.loc svg{width:5px;height:7px}
.stars{position:absolute;left:137px;top:40px;display:flex;align-items:center;gap:1px;font-size:6.5px;color:#555}
.stars svg{width:7px;height:7px}
.stars em{font-style:normal;margin-left:4px}
.amenities{position:absolute;left:134px;top:68px;display:grid;grid-template-columns:repeat(3,28px);row-gap:5px}
.amenity{display:flex;flex-direction:column;align-items:center;gap:1px;font-size:3.6px;line-height:4px;color:var(--blue);text-align:center}
.amenity svg{width:15px;height:15px}
.offer{position:absolute;left:248px;top:24px;font-size:7.5px;line-height:11.5px;color:#444}
.price-tag{position:absolute;left:247px;top:58px;font-size:28px;font-weight:300;color:var(--blue);line-height:34px}
.rooms{position:absolute;left:248px;top:96px;width:85px;height:23px;font-size:7.5px;gap:8px}
.rooms svg{width:4px;height:7px}
.more-btn{left:413px;top:761px;width:84px;height:23px;font-size:7.5px}

/* steps band */
.band{left:0;top:802px;width:731px;height:226px;background:linear-gradient(160deg,var(--band-a),var(--band-b) 60%,#2b6fb6)}
.band-art{position:absolute;inset:0;background:linear-gradient(180deg,rgba(255,255,255,0) 55%,rgba(255,255,255,.08))}
.band h2{position:absolute;top:10px;width:100%;text-align:center;font-size:24px;font-weight:400;color:#fff;letter-spacing:.2px}
.band .sub{position:absolute;top:37px;width:100%;text-align:center;font-size:9px;font-weight:300;color:#fff}
.band .rule{position:absolute;left:105px;width:521px;background:rgba(255,255,255,.45)}
.step{position:absolute;top:73px;width:160px;text-align:center;color:#fff}
.step .num{width:36px;height:30px;margin:0 auto;background:var(--green);border-radius:2px;font-size:18px;font-weight:600;display:flex;align-items:center;justify-content:center}
.step h3{font-size:12.5px;font-weight:600;margin-top:10px}
.step hr{width:18px;border:0;border-top:1px solid rgba(255,255,255,.6);margin:5px auto 6px}
.step p{font-size:7px;line-height:13px;font-weight:300}
.band .dots{position:absolute;top:1011px;bottom:auto}
.band-dots{position:absolute;top:208px;width:100%;display:flex;justify-content:center;gap:4px}
.band-dots i{width:2.5px;height:2.5px;border-radius:50%;background:#fff}
.band-dots i:first-child{width:4px;height:4px;margin-top:-.5px}

/* footer */
.site-footer{left:0;top:1028px;width:731px;height:172px;background:var(--footer);color:#ddd}
.foot-brand{position:absolute;left:105px;top:11px;display:flex;align-items:center;gap:4px;font-size:11px;font-weight:600;color:#eee}
.foot-brand i{width:10px;height:10px;background:#bbb;display:block}
.site-footer .rule{position:absolute;left:105px;width:521px;background:#555}
.fcol{position:absolute;top:46px}
.fcol h5{font-size:7.5px;font-weight:600;color:#eee;letter-spacing:.1px}
.fcol ul{list-style:none;margin-top:6px}
.fcol li{font-size:7px;line-height:13.7px;color:#ddd;display:flex;align-items:center;gap:4px}
.fcol li svg{width:6px;height:6px;fill:#ddd}
.news p{font-size:7px;margin-top:8px}
.news form{display:flex;gap:4px;margin-top:8px}
.news .email{width:102px;height:18px;background:#fff;border-radius:1px;font-size:6.5px;color:#666;display:flex;align-items:center;padding-left:5px}
.news .sign{width:46px;height:18px;font-size:6.5px}
.news small{display:block;font-size:5.3px;line-height:8px;margin-top:7px;color:#ccc;width:150px}
.copy{position:absolute;top:161px;width:100%;text-align:center;font-size:5.8px;color:#ddd}
</style>
</head>
<body>

<header class="site-header abs">
  <div class="brand abs"><i></i>Caybound</div>
  <nav class="main-nav abs">
    <span>Discover Cayman</span><span>Things to Do</span><span>Hotels</span><span>Trip Planner</span><span>Map</span><span>Contact Us</span>
  </nav>
  <div class="select abs" style="left:482px;width:57px">Destinations <svg viewBox="0 0 10 6"><path d="M1 1l4 4 4-4" fill="none" stroke="#9bcb3b" stroke-width="1.5"/></svg></div>
  <div class="select abs" style="left:544px;width:31px">USD <svg viewBox="0 0 10 6"><path d="M1 1l4 4 4-4" fill="none" stroke="#9bcb3b" stroke-width="1.5"/></svg></div>
  <div class="login btn abs">Login</div>
</header>

<section class="search-bar">
  <div class="search-field abs" style="left:105px;width:114px">
    <svg viewBox="0 0 10 14"><path d="M5 0a5 5 0 0 0-5 5c0 4 5 9 5 9s5-5 5-9a5 5 0 0 0-5-5zm0 7a2 2 0 1 1 0-4 2 2 0 0 1 0 4z"/></svg>
    <div><small>Going to</small><b>Cayman Islands</b></div>
  </div>
  <div class="search-field abs" style="left:224px;width:82px">
    <svg viewBox="0 0 12 12"><path d="M1 2h10v10H1zM3 0h1.5v3H3zM7.5 0H9v3H7.5z"/><path d="M2.5 5h7v5.5h-7z" fill="#fff"/><path d="M3.5 6h1.5v1.5H3.5zM6 6h1.5v1.5H6zM3.5 8.3h1.5v1.5H3.5z"/></svg>
    <div><small>Check-in</small><b>Aug 1st</b></div>
  </div>
  <div class="search-field abs" style="left:311px;width:82px">
    <svg viewBox="0 0 12 12"><path d="M1 2h10v10H1zM3 0h1.5v3H3zM7.5 0H9v3H7.5z"/><path d="M2.5 5h7v5.5h-7z" fill="#fff"/><path d="M3.5 6h1.5v1.5H3.5zM6 6h1.5v1.5H6zM3.5 8.3h1.5v1.5H3.5z"/></svg>
    <div><small>Check-out</small><b>Aug 3rd</b></div>
  </div>
  <div class="search-field abs" style="left:398px;width:113px">
    <svg viewBox="0 0 12 12"><circle cx="6" cy="3" r="3"/><path d="M0 12c0-4 3-5 6-5s6 1 6 5z"/></svg>
    <div><small>Guests &amp; Rooms</small><b>2 rooms, 3 guests</b></div>
  </div>
  <div class="search-btn btn abs">Search</div>
</section>
<div class="rule abs" style="left:105px;top:68px;width:521px"></div>

<aside>
  <div class="map-card abs">
    <div class="map-area" role="img" aria-label="Map of Grand Cayman showing the hotel locations"></div>
    <p>Map</p>
  </div>
  <div class="rule abs" style="left:105px;top:214px;width:160px"></div>

  <div class="filters abs">
    <h4 class="filter-title"><svg width="9" height="8" viewBox="0 0 9 8"><path d="M1 3v5M4 0v8M7 4v4" stroke="#1a6fd6" stroke-width="1.4"/></svg>Filter:</h4>
    <div class="price">Price: <span>Min $</span>-<span>Max $</span></div>

    <div class="group">
      <h4>Star Rating:</h4>
      <ul class="checks">
        <li><i class="box on"></i>5 Stars</li>
        <li><i class="box on"></i>4 Stars</li>
        <li><i class="box"></i>3 Stars</li>
        <li><i class="box"></i>2 Stars</li>
        <li><i class="box"></i>1 Stars</li>
      </ul>
    </div>
    <div class="group">
      <h4>Property Type</h4>
      <ul class="checks">
        <li><i class="box"></i>Hotel Resort</li>
        <li><i class="box on"></i>Hotel</li>
        <li><i class="box"></i>All-Inclusive Resort</li>
        <li><i class="box"></i>Townhouse</li>
        <li><i class="box on"></i>Agritourism</li>
        <li><i class="box"></i>Cottage</li>
        <li><i class="box"></i>Residence</li>
        <li><i class="box"></i>Condo</li>
      </ul>
    </div>
    <div class="group">
      <h4>Amenities</h4>
      <ul class="checks">
        <li><i class="box on"></i>Breakfast Included</li>
        <li><i class="box"></i>Air Conditioned</li>
        <li><i class="box"></i>Free Wifi</li>
        <li><i class="box"></i>Pool</li>
        <li><i class="box"></i>Free Airport Shuttle</li>
        <li><i class="box"></i>Water Park</li>
        <li><i class="box on"></i>Spa</li>
        <li style="opacity:.7"><i class="box"></i>Gym</li>
        <li class="fade"><i class="box"></i>Pet Friendly</li>
      </ul>
      <div class="see-link">See More</div>
    </div>
    <div class="group">
      <h4>Location</h4>
      <ul class="checks">
        <li><i class="box"></i>Cayman Islands</li>
        <li><i class="box on"></i>Seven Mile Beach</li>
        <li><i class="box"></i>East End</li>
        <li><i class="box on"></i>Cayman Brac Island</li>
      </ul>
    </div>
  </div>
  <div class="filter-btn btn abs">Filter Results</div>
</aside>
<div class="divider-v abs"></div>

<svg width="0" height="0" style="position:absolute">
  <defs>
    <symbol id="star" viewBox="0 0 10 10"><path d="M5 0l1.5 3.3 3.5.3-2.7 2.3.9 3.5L5 7.5 1.8 9.4l.9-3.5L0 3.6l3.5-.3z"/></symbol>
    <symbol id="pin" viewBox="0 0 10 14"><path d="M5 0a5 5 0 0 0-5 5c0 4 5 9 5 9s5-5 5-9a5 5 0 0 0-5-5zm0 7a2 2 0 1 1 0-4 2 2 0 0 1 0 4z" fill="#1a6fd6"/></symbol>
    <symbol id="pool" viewBox="0 0 16 16"><path d="M5 2v8M10 2v8M5 5h5M5 8h5M1 11c2-1 3 1 5 0s3 1 5 0 3 1 4 0M1 14c2-1 3 1 5 0s3 1 5 0 3 1 4 0" fill="none" stroke="#1a6fd6" stroke-width="1.2"/></symbol>
    <symbol id="wifi" viewBox="0 0 16 16"><path d="M1 6a10 10 0 0 1 14 0M3.5 8.5a6.5 6.5 0 0 1 9 0M6 11a3 3 0 0 1 4 0" fill="none" stroke="#1a6fd6" stroke-width="1.6"/><circle cx="8" cy="13.5" r="1.3" fill="#1a6fd6"/></symbol>
    <symbol id="tennis" viewBox="0 0 16 16"><ellipse cx="10" cy="6" rx="4.5" ry="4.5" fill="none" stroke="#1a6fd6" stroke-width="1.3"/><path d="M7 9l-5 5" stroke="#1a6fd6" stroke-width="1.8"/><circle cx="3" cy="4" r="1.5" fill="#1a6fd6"/></symbol>
    <symbol id="parking" viewBox="0 0 16 16"><rect x="1" y="1" width="14" height="14" rx="2" fill="#1a6fd6"/><path d="M6 12V4h3a2.3 2.3 0 0 1 0 4.6H6" fill="none" stroke="#fff" stroke-width="1.8"/></symbol>
    <symbol id="fitness" viewBox="0 0 16 16"><circle cx="9" cy="2.5" r="1.8" fill="#1a6fd6"/><path d="M8 5L5 9l4 1-1 5M8 5l3 3 3-1M3 14h10" fill="none" stroke="#1a6fd6" stroke-width="1.5"/></symbol>
    <symbol id="paw" viewBox="0 0 16 16"><g fill="#1a6fd6"><ellipse cx="8" cy="11" rx="4" ry="3.5"/><circle cx="3" cy="7" r="1.8"/><circle cx="6" cy="3.5" r="1.8"/><circle cx="10" cy="3.5" r="1.8"/><circle cx="13" cy="7" r="1.8"/></g></symbol>
    <symbol id="chev" viewBox="0 0 6 10"><path d="M1 1l4 4-4 4" fill="none" stroke="#fff" stroke-width="1.4"/></symbol>
    <symbol id="chevl" viewBox="0 0 6 10"><path d="M5 1L1 5l4 4" fill="none" stroke="#fff" stroke-width="1.4"/></symbol>
  </defs>
</svg>

<main>
  <!-- card 1 -->
  <article class="hotel abs" style="top:77px">
    <div class="photo" role="img" aria-label="Wooden boardwalk through dunes to a turquoise sea" style="background:linear-gradient(180deg,#8ab0c0 0%,#3aa8b4 38%,#1f8f9c 50%,#c7b8a0 70%,#a8957b 100%)"></div>
    <span class="arrow" style="left:4px"><svg><use href="#chevl"/></svg></span><span class="arrow" style="left:108px"><svg><use href="#chev"/></svg></span>
    <div class="dots"><i></i><i></i><i></i><i></i><i></i></div>
    <h3>Harbor Suites Seven Mile Beach</h3><span class="reviews">Reviews</span>
    <div class="loc"><svg><use href="#pin"/></svg>Seven Mile Beach</div>
    <div class="stars"><svg fill="#1a6fd6"><use href="#star"/></svg><svg fill="#1a6fd6"><use href="#star"/></svg><svg fill="#1a6fd6"><use href="#star"/></svg><svg fill="#1a6fd6"><use href="#star"/></svg><svg fill="#c9d2de"><use href="#star"/></svg><em>4 out of 5 Stars</em></div>
    <div class="amenities">
      <div class="amenity"><svg><use href="#pool"/></svg>Swimming<br>Pool</div><div class="amenity"><svg><use href="#wifi"/></svg>Free Wifi</div><div class="amenity"><svg><use href="#tennis"/></svg>Tennis Court</div>
      <div class="amenity"><svg><use href="#parking"/></svg>Free Parking</div><div class="amenity"><svg><use href="#fitness"/></svg>Fitness Center</div><div class="amenity"><svg><use href="#paw"/></svg>Kennel</div>
    </div>
    <div class="offer">Free Cancellation<br>Reserve now, Pay later<br>Starting at:</div>
    <div class="price-tag">$120</div>
    <div class="rooms btn">Show Rooms <svg><use href="#chev"/></svg></div>
  </article>

  <!-- card 2 -->
  <article class="hotel abs" style="top:214px">
    <div class="photo" role="img" aria-label="Palm trees leaning over a tropical beach" style="background:linear-gradient(180deg,#e9eef2 0%,#c9d8de 35%,#3fa3b7 50%,#4b7a3a 70%,#7a8f5a 100%)"></div>
    <span class="arrow" style="left:4px"><svg><use href="#chevl"/></svg></span><span class="arrow" style="left:108px"><svg><use href="#chev"/></svg></span>
    <div class="dots"><i></i><i></i><i></i><i></i><i></i></div>
    <h3>Amara Garden Suite</h3><span class="reviews">Reviews</span>
    <div class="loc"><svg><use href="#pin"/></svg>Cayman Islands</div>
    <div class="stars"><svg fill="#1a6fd6"><use href="#star"/></svg><svg fill="#1a6fd6"><use href="#star"/></svg><svg fill="#1a6fd6"><use href="#star"/></svg><svg fill="#c9d2de"><use href="#star"/></svg><svg fill="#c9d2de"><use href="#star"/></svg><em>3 out of 5 Stars</em></div>
    <div class="amenities">
      <div class="amenity"><svg><use href="#pool"/></svg>Swimming<br>Pool</div><div class="amenity"><svg><use href="#wifi"/></svg>Free Wifi</div><div class="amenity"><svg><use href="#tennis"/></svg>Tennis Court</div>
      <div class="amenity"><svg><use href="#parking"/></svg>Free Parking</div><div class="amenity"><svg><use href="#fitness"/></svg>Fitness Center</div><div class="amenity"><svg><use href="#paw"/></svg>Kennel</div>
    </div>
    <div class="offer">Free Cancellation<br>Reserve now, Pay later<br>Starting at:</div>
    <div class="price-tag">$140</div>
    <div class="rooms btn">Show Rooms <svg><use href="#chev"/></svg></div>
  </article>

  <!-- card 3 -->
  <article class="hotel abs" style="top:351px">
    <div class="photo" role="img" aria-label="Sunset over gentle waves on a sandy shore" style="background:linear-gradient(180deg,#a9bfcd 0%,#e6d6bf 35%,#9fb6c0 50%,#cdd8d8 65%,#d8c7b0 100%)"></div>
    <span class="arrow" style="left:4px"><svg><use href="#chevl"/></svg></span><span class="arrow" style="left:108px"><svg><use href="#chev"/></svg></span>
    <div class="dots"><i></i><i></i><i></i><i></i><i></i></div>
    <h3>Coral Cove Resort</h3><span class="reviews">Reviews</span>
    <div class="loc"><svg><use href="#pin"/></svg>Grand Cayman</div>
    <div class="stars"><svg fill="#1a6fd6"><use href="#star"/></svg><svg fill="#1a6fd6"><use href="#star"/></svg><svg fill="#1a6fd6"><use href="#star"/></svg><svg fill="#1a6fd6"><use href="#star"/></svg><svg fill="#1a6fd6"><use href="#star"/></svg><em>5 out of 5 Stars</em></div>
    <div class="amenities">
      <div class="amenity"><svg><use href="#pool"/></svg>Swimming<br>Pool</div><div class="amenity"><svg><use href="#wifi"/></svg>Free Wifi</div><div class="amenity"><svg><use href="#tennis"/></svg>Tennis Court</div>
      <div class="amenity"><svg><use href="#parking"/></svg>Free Parking</div><div class="amenity"><svg><use href="#fitness"/></svg>Fitness Center</div><div class="amenity"><svg><use href="#paw"/></svg>Kennel</div>
    </div>
    <div class="offer">Free Cancellation<br>Reserve now, Pay later<br>Starting at:</div>
    <div class="price-tag">$110</div>
    <div class="rooms btn">Show Rooms <svg><use href="#chev"/></svg></div>
  </article>

  <!-- card 4 -->
  <article class="hotel abs" style="top:488px">
    <div class="photo" role="img" aria-label="Two blue beach chairs on the sand facing the sea" style="background:linear-gradient(180deg,#4a86b4 0%,#8db2cc 38%,#3d7fa8 50%,#5a88a8 70%,#a89c8a 100%)"></div>
    <span class="arrow" style="left:4px"><svg><use href="#chevl"/></svg></span><span class="arrow" style="left:108px"><svg><use href="#chev"/></svg></span>
    <div class="dots"><i></i><i></i><i></i><i></i><i></i></div>
    <h3>Seaglass Beach Resort</h3><span class="reviews">Reviews</span>
    <div class="loc"><svg><use href="#pin"/></svg>Grand Cayman</div>
    <div class="stars"><svg fill="#1a6fd6"><use href="#star"/></svg><svg fill="#1a6fd6"><use href="#star"/></svg><svg fill="#1a6fd6"><use href="#star"/></svg><svg fill="#7fa6da"><use href="#star"/></svg><svg fill="#c9d2de"><use href="#star"/></svg><em>3.4 out of 5 Stars</em></div>
    <div class="amenities">
      <div class="amenity"><svg><use href="#pool"/></svg>Swimming<br>Pool</div><div class="amenity"><svg><use href="#wifi"/></svg>Free Wifi</div><div class="amenity"><svg><use href="#tennis"/></svg>Tennis Court</div>
      <div class="amenity"><svg><use href="#parking"/></svg>Free Parking</div><div class="amenity"><svg><use href="#fitness"/></svg>Fitness Center</div><div class="amenity"><svg><use href="#paw"/></svg>Kennel</div>
    </div>
    <div class="offer">Free Cancellation<br>Reserve now, Pay later<br>Starting at:</div>
    <div class="price-tag">$180</div>
    <div class="rooms btn">Show Rooms <svg><use href="#chev"/></svg></div>
  </article>

  <!-- card 5 -->
  <article class="hotel abs" style="top:626px">
    <div class="photo" role="img" aria-label="Orange beach umbrellas over turquoise loungers" style="background:linear-gradient(180deg,#a8c2d8 0%,#d9e3ea 30%,#e8923a 48%,#2fb7c2 70%,#cbbfae 100%)"></div>
    <span class="arrow" style="left:4px"><svg><use href="#chevl"/></svg></span><span class="arrow" style="left:108px"><svg><use href="#chev"/></svg></span>
    <div class="dots"><i></i><i></i><i></i><i></i><i></i></div>
    <h3>Palm Grove Grand Cayman</h3><span class="reviews">Reviews</span>
    <div class="loc"><svg><use href="#pin"/></svg>Cayman Brac Island</div>
    <div class="stars"><svg fill="#1a6fd6"><use href="#star"/></svg><svg fill="#1a6fd6"><use href="#star"/></svg><svg fill="#1a6fd6"><use href="#star"/></svg><svg fill="#1a6fd6"><use href="#star"/></svg><svg fill="#c9d2de"><use href="#star"/></svg><em>4 out of 5 Stars</em></div>
    <div class="amenities">
      <div class="amenity"><svg><use href="#pool"/></svg>Swimming<br>Pool</div><div class="amenity"><svg><use href="#wifi"/></svg>Free Wifi</div><div class="amenity"><svg><use href="#tennis"/></svg>Tennis Court</div>
      <div class="amenity"><svg><use href="#parking"/></svg>Free Parking</div><div class="amenity"><svg><use href="#fitness"/></svg>Fitness Center</div><div class="amenity"><svg><use href="#paw"/></svg>Kennel</div>
    </div>
    <div class="offer">Free Cancellation<br>Reserve now, Pay later<br>Starting at:</div>
    <div class="price-tag">$220</div>
    <div class="rooms btn">Show Rooms <svg><use href="#chev"/></svg></div>
  </article>

  <div class="more-btn btn abs">See More</div>
</main>
<div class="rule abs" style="left:105px;top:793px;width:521px"></div>

<section class="band abs">
  <div class="band-art" role="img" aria-label="Beach chairs by the sea under a blue tint"></div>
  <h2>BOOKING A HOTEL IS SO EASY NOW!</h2>
  <p class="sub">Your Dream Holiday is Just One Click Away</p>
  <div class="rule" style="top:60px"></div>
  <div class="step" style="left:112px">
    <div class="num">1</div><h3>Select Your Hotel</h3><hr>
    <p>You can use the filters on the right side to select your perfect holiday resident. Also you can find all the details about the hotel in the hotel pages.</p>
  </div>
  <div class="step" style="left:285px">
    <div class="num">2</div><h3>Select Payment Options</h3><hr>
    <p>After selection your dream vacation resident, you will be directed to the payments section where you can pay with various trustful methods.</p>
  </div>
  <div class="step" style="left:459px">
    <div class="num">3</div><h3>Enjoy Your Holiday</h3><hr>
    <p>We list only the best hotels in our website. Enjoy our services and remember to leave a rating.</p>
  </div>
  <div class="rule" style="top:198px"></div>
  <div class="band-dots"><i></i><i></i><i></i><i></i><i></i></div>
</section>

<footer class="site-footer abs">
  <div class="foot-brand"><i></i>Caybound</div>
  <div class="rule" style="top:33px"></div>
  <div class="fcol" style="left:105px">
    <h5>SITEMAP</h5>
    <ul><li>Discover Cayman</li><li>Things to Do</li><li>Hotels</li><li>Trip Planner</li><li>Map</li><li>Contact Us</li></ul>
  </div>
  <div class="fcol" style="left:213px">
    <h5>INFORMATION</h5>
    <ul><li>Support</li><li>Account</li><li>Terms &amp; Conditions</li><li>Privacy Policy</li><li>Leave a Review</li></ul>
  </div>
  <div class="fcol news" style="left:342px">
    <h5>SIGN UP TO OUR NEWSLETTER</h5>
    <p>Receive special offers and first look at new deals</p>
    <div class="form" style="display:flex;gap:4px;margin-top:8px"><span class="email">Your email...</span><span class="sign btn">Sign Up</span></div>
    <small>By signing up, you agree to receive marketing emails and our privacy policy</small>
  </div>
  <div class="fcol" style="left:563px">
    <h5>GET CONNECTED</h5>
    <ul>
      <li><svg viewBox="0 0 6 6"><circle cx="3" cy="3" r="3"/></svg>Friendbook</li>
      <li><svg viewBox="0 0 6 6"><circle cx="3" cy="3" r="3"/></svg>Chirper</li>
      <li><svg viewBox="0 0 6 6"><circle cx="3" cy="3" r="3"/></svg>Snapgram</li>
      <li><svg viewBox="0 0 6 6"><circle cx="3" cy="3" r="3"/></svg>Linkpro</li>
      <li><svg viewBox="0 0 6 6"><circle cx="3" cy="3" r="3"/></svg>Pinboard</li>
    </ul>
  </div>
  <div class="rule" style="top:157px"></div>
  <p class="copy">© Copyright 2019 Caybound. All Rights Reserved</p>
</footer>

</body>
</html>
```